Poster Design For Obstacle Run

Design a poster for the Copper Dune Obstacle run.
Text: Copper Dune Obstacle Run. May 12th, 2018. Sittard. www.copperdunerun.nl. I have added a lot of pictures.
Furthermore, the logo should be included. As an example I included a poster from the valkor race that we really like (valkor team challenge) and also. Feel free to take a look at our website for inspiration: www.copperdunerun.nl

```html
<!DOCTYPE html>
<html lang="en">
<head>
<meta charset="utf-8">
<title>Copper Dune Obstacle Run – Poster</title>
<link rel="stylesheet" href="https://fonts.googleapis.com/css2?family=Alfa+Slab+One&family=Black+Ops+One&family=Montserrat:wght@400&display=swap">
<style>
  :root {
    --ink-white: #f4f1ec;
    --race-red: #e3261a;
    --deep-red: #8e1109;
    --earth-dark: #140d08;
    --earth-mid: #4a3626;
    --earth-light: #8a715c;
    --skin-warm: #9a5a3a;
  }
  html, body {
    margin: 0;
    padding: 0;
    overflow: hidden;
    background: var(--earth-dark);
  }
  .poster {
    position: relative;
    width: 1200px;
    height: 802px;
    overflow: hidden;
    background: var(--earth-dark);
  }
  .action-photo {
    position: absolute;
    inset: 0;
    background:
      radial-gradient(ellipse 10% 40% at 62% 28%, rgba(154,90,58,0.75), transparent 80%),
      radial-gradient(ellipse 6% 22% at 8% 42%, rgba(154,90,58,0.55), transparent 80%),
      radial-gradient(ellipse 38% 42% at 38% 22%, rgba(8,5,3,0.95), transparent 75%),
      radial-gradient(ellipse 22% 30% at 22% 42%, rgba(10,6,4,0.85), transparent 75%),
      radial-gradient(ellipse 18% 22% at 70% 18%, rgba(10,6,4,0.9), transparent 75%),
      radial-gradient(ellipse 40% 40% at 88% 40%, var(--earth-light), transparent 75%),
      radial-gradient(ellipse 45% 35% at 60% 95%, #b9a594, transparent 75%),
      radial-gradient(ellipse 30% 50% at 5% 70%, var(--earth-mid), transparent 80%),
      linear-gradient(160deg, #3a2a1e 0%, #2a1d14 40%, #5b4636 75%, #6f5948 100%);
  }
  .brand-mark {
    position: absolute;
    left: 300px;
    top: 372px;
    display: flex;
    align-items: center;
    gap: 12px;
  }
  .brand-mark__dot {
    width: 28px;
    height: 28px;
    border-radius: 50%;
    background: var(--race-red);
  }
  .brand-mark__name {
    font-family: "Alfa Slab One", serif;
    font-size: 30px;
    color: var(--ink-white);
  }
  .title-run {
    position: absolute;
    left: 600px;
    top: 340px;
    margin: 0;
    font-family: "Black Ops One", sans-serif;
    font-size: 400px;
    line-height: 1;
    color: var(--race-red);
    transform-origin: left top;
    transform: scaleX(0.57) skewX(-14deg);
    text-shadow: 5px 5px 0 var(--deep-red);
    white-space: nowrap;
  }
  .title {
    position: absolute;
    left: 56px;
    top: 470px;
    margin: 0;
    font-family: "Alfa Slab One", serif;
    font-weight: 400;
    font-size: 76px;
    line-height: 98px;
    color: var(--ink-white);
    text-shadow: 3px 3px 0 var(--deep-red);
    transform-origin: left top;
    transform: scaleX(0.82);
    white-space: nowrap;
  }
  .title__line { display: block; }
  .event-info {
    position: absolute;
    left: 60px;
    top: 676px;
    margin: 0;
    display: flex;
    align-items: baseline;
    font-family: "Montserrat", sans-serif;
    font-size: 27px;
    color: var(--ink-white);
  }
  .event-info__city {
    letter-spacing: 7px;
    width: 214px;
  }
  .event-info__date { width: 288px; }
</style>
</head>
<body>
  <main class="poster">
    <div class="action-photo" role="img" aria-label="Close-up action photo of a muddy obstacle runner crouching in a cloud of dust and dirt"></div>

    <div class="brand-mark">
      <span class="brand-mark__dot"></span>
      <span class="brand-mark__name">Copper Dune</span>
    </div>

    <p class="title-run" aria-hidden="true">RUN</p>
    <h1 class="title">
      <span class="title__line">COPPER DUNE</span>
      <span class="title__line">OBSTACLE</span>
    </h1>

    <p class="event-info">
      <span class="event-info__city">SITTARD</span>
      <span class="event-info__date">May 12th, 2018</span>
      <span class="event-info__web">www.copperdunerun.nl</span>
    </p>
  </main>
</body>
</html>
```